Holiday Rental Leaflet

Want a DL size double sided leaflet to distribute via local businesses, markets, family and friends
HOLIDAY RENTALCarrickalinga - 17 Brindle Street Sleeps 8-10 (2 Queen, 1 Double, 2 bunks), 4 bedrooms, BIR to all bedrooms 2 Bathrooms, one with bath, 2 toilets Open Plan Lounge/Dining/Kitchen area Dining Table for 8 peopleReverse cycle airconditionerSlow combustion wood heaterTV/DVD, CD/RadioKitchen has m/wave, oven, fridge/freezer, dishwasherBBQ providedTimber decking with 2 outside tables and 12 chairs Washing Machine and dryer provided One street back from beach Smoke free zone No Pets
For further information or to book contact Joan on 0491 287 306 or email joanfarrow27@velmarnet.com.au

Industry/Entity Type

Kitchen

Requirements
Nice to have
• Have sent a variety of photos of the house. No need to use all of them, pick out the most relevant for the leaflet.

```html
<!DOCTYPE html>
<html lang="en">
<head>
<meta charset="utf-8">
<title>Holiday Rental – Carrickalinga</title>
<link href="https://fonts.googleapis.com/css2?family=Cinzel+Decorative:wght@700&family=Questrial&family=Arimo:wght@400;700&display=swap" rel="stylesheet">
<style>
  :root {
    --sky-light: #35b4ec;
    --sky-mid: #1d8fd6;
    --sky-deep: #0d5ea8;
    --title-yellow: #f6ea1a;
    --sub-yellow: #e8f03a;
    --banner-yellow: #fff200;
    --ink: #0a1a2a;
    --white: #ffffff;
  }
  html, body {
    margin: 0;
    padding: 0;
    width: 1200px;
    height: 850px;
    overflow: hidden;
  }
  .leaflet {
    position: relative;
    width: 1200px;
    height: 850px;
    overflow: hidden;
    background: radial-gradient(ellipse at 50% 45%, var(--sky-light) 0%, var(--sky-mid) 55%, var(--sky-deep) 100%);
    font-family: "Questrial", Arial, sans-serif;
    color: var(--white);
  }
  .title {
    position: absolute;
    left: 36px;
    top: 24px;
    margin: 0;
    font-family: "Cinzel Decorative", Georgia, serif;
    font-weight: 700;
    font-size: 91px;
    letter-spacing: 2px;
    line-height: 1;
    color: var(--title-yellow);
    white-space: nowrap;
  }
  .address {
    position: absolute;
    left: 38px;
    top: 128px;
    margin: 0;
    font-family: "Arimo", Arial, sans-serif;
    font-size: 39px;
    font-weight: 400;
    color: var(--sub-yellow);
    white-space: nowrap;
  }
  .features {
    position: absolute;
    margin: 0;
    font-size: 18.5px;
    line-height: 23.5px;
    text-transform: uppercase;
    letter-spacing: 0.2px;
    white-space: nowrap;
  }
  .features--sleeping { left: 54px; top: 296px; }
  .features--living { left: 54px; top: 630px; }
  .features--laundry { left: 964px; top: 94px; }
  .features--kitchen { left: 920px; top: 412px; }
  .features--kitchen-more { left: 920px; top: 490px; }
  .features--outdoor { left: 920px; top: 550px; }
  .photo {
    position: absolute;
    border: 6px solid var(--white);
    box-shadow: 0 4px 14px rgba(0, 0, 0, 0.35);
  }
  .photo--house {
    left: 342px; top: 212px; width: 528px; height: 402px;
    background: linear-gradient(180deg, #cfd8dc 0%, #9aa59a 35%, #6b7f4c 70%, #7e8f4f 100%);
  }
  .photo--beach {
    left: 757px; top: 136px; width: 177px; height: 116px;
    background: linear-gradient(180deg, #d8dfe6 0%, #6d8aa2 45%, #4e6a80 60%, #7d8257 100%);
  }
  .photo--heater {
    left: 836px; top: 262px; width: 128px; height: 110px;
    background: linear-gradient(180deg, #b98a5e 0%, #8a5d3a 50%, #3d3330 100%);
  }
  .photo--lounge {
    left: 220px; top: 442px; width: 202px; height: 152px;
    background: linear-gradient(135deg, #d9c9ad 0%, #9a7a5a 45%, #2c2a2c 100%);
  }
  .photo--bathroom {
    left: 318px; top: 572px; width: 166px; height: 144px;
    background: linear-gradient(180deg, #f1f1ee 0%, #d6d7d4 60%, #b9bbb8 100%);
  }
  .booking {
    position: absolute;
    left: 576px;
    top: 680px;
    width: 624px;
    height: 140px;
  }
  .booking__band {
    position: absolute;
    inset: 0;
  }
  .booking__text {
    position: absolute;
    right: 26px;
    top: 12px;
    margin: 0;
    text-align: right;
    font-family: "Arimo", Arial, sans-serif;
    color: var(--ink);
    font-size: 22px;
    line-height: 38px;
    white-space: nowrap;
  }
  .booking__phone {
    font-weight: 700;
    font-size: 35px;
    vertical-align: -2px;
  }
  .booking__email {
    font-weight: 700;
  }
</style>
</head>
<body>
<main class="leaflet">
  <h1 class="title">HOLIDAY RENTAL</h1>
  <p class="address">Carrickalinga - 17 Brindle Street</p>

  <p class="features features--sleeping">Sleeps 8-10<br>(2 Queen, 1 Double,<br>2 Bunks), 4 Bedrooms,<br>BIR to all bedrooms<br>2 Bathrooms, one with<br>bath, 2 toilets</p>

  <p class="features features--laundry">Washing machine<br>and dryer<br>provided one<br>street back from<br>beach smoke<br>free zone no pets</p>

  <p class="features features--kitchen">TV/DVD, CD/Radio<br>kitchen has m/wave,</p>
  <p class="features features--kitchen-more">Oven, fridge/freezer,<br>dishwasher</p>
  <p class="features features--outdoor">BBQ provided<br>timber decking with<br>2 outside tables<br>and 12 chairs</p>

  <p class="features features--living">Open plan lounge/<br>dining/kitchen area<br>dining table for<br>8 people, reverse cycle<br>airconditioner<br>slow combustion wood heater</p>

  <div class="photo photo--beach" role="img" aria-label="Photo of the ocean view over the beach from the street"></div>
  <div class="photo photo--heater" role="img" aria-label="Photo of the slow combustion wood heater"></div>
  <div class="photo photo--house" role="img" aria-label="Photo of the elevated timber holiday house with front lawn and sprinkler"></div>
  <div class="photo photo--lounge" role="img" aria-label="Photo of the lounge room with leather sofas and bookshelf"></div>
  <div class="photo photo--bathroom" role="img" aria-label="Photo of the white tiled bathroom with bath and toilet"></div>

  <section class="booking">
    <svg class="booking__band" width="624" height="140" viewBox="0 0 624 140" aria-hidden="true">
      <polygon points="0,0 624,0 624,140 20,140 40,70" fill="var(--banner-yellow)"/>
    </svg>
    <p class="booking__text">
      For further information or to book<br>
      contact Joan on <span class="booking__phone">0491 287 306</span><br>
      or email <span class="booking__email">joanfarrow27@velmarnet.com.au</span>
    </p>
  </section>
</main>
</body>
</html>
```